Psychologist in Private Practice Needs a Website Update

Project Description:
Hello talented designers! My current website, www.junetillard.com, needs a fresh, boho-modern makeover that highlights the warm, welcoming nature of my holistic therapy practice. I want a website that has a serene, boho- modern design, appealing to clients seeking individual therapy, couples therapy, and family counseling.

I’d also like to prepare for a future second site focused exclusively on couples and family therapy. Both sites should be interconnected, so I’m looking for design suggestions that seamlessly link them together while maintaining a cohesive brand look and feel.

Key Objectives:

Boho-Modern Aesthetic: Incorporate natural textures, neutral or earthy tones, and clean lines that capture a modern, inviting vibe.

Responsive Design: Ensure the website is user-friendly on desktop, tablet, and mobile devices.

Clear Service Offerings: Prominently feature my three distinct services: individual therapy, couples therapy, and family counseling.

Interlinked Future Site: Provide ideas on how to cross-link this site with a second site focused on couples and family therapy.

User Experience (UX): Make the site simple to navigate, with intuitive placement of content that speaks to potential clients’ needs.

SEO-Friendly: Implement best practices for structure, site speed, and keyword usage to boost online visibility.

What I Have Now:
Existing website: www.junetillard.com
Basic content and a logo that can be refined or updated to match the boho-modern feel
Rough style guide with brand elements open to a fresh interpretation

Preferred Style/Tone:
Boho-modern with earthy tones, subtle textures, and clean typography
Warm, empathetic, and approachable to align with the nature of therapy services
Slightly artistic or organic elements that evoke calm and connection

Potential for an ongoing design relationship!
Updates

Need extra days to review

Target Market(s)

I have a high functioning, professional clientele who doctors, lawyers, and leaders in their field.

Industry/Entity Type

healthcare/mental health

Coding

Coded - Design and coding required

Font styles to use
Other font styles liked:
• cormorant garamond for headers and Source Sans Pro for supporting text

Colors

Designer to choose colors to be used in the design.

Requirements
Must have
• Open, Harmonious Layout I’d like the overall design to feel upscale, humanistic, open and harmonious, with minimal divisions of space. Rather than traditional section dividers, please consider using images, subtle shifts in color, typography, or spacing to define sections. Hero Image & Inspiration Ideally, the first (hero) image should evoke a sense of awe or inspiration. Focus on simplicity and elegance so the design feels spacious and inviting, allowing the content and imagery to really stand out. Natural Flow Wherever possible, let the design elements flow naturally into each other, creating a sense of unity and cohesion throughout the site.
Nice to have
• 1. Full-Width Hero Image: • The homepage should feature a full-width hero image that extends edge-to-edge across the screen for a modern and visually immersive effect. • This image should set the tone for the website, reflecting a calming, humanistic/natural, and upscale feel. It could include subtle overlays or gradients to enhance readability of text and navigation elements. Ideally, this image should have one or two people in nature. The image could be slightly transparent to allow the text "holistic therapy" and the tagline "an integrative approach to transformation" to be easily visible. Please help me find a breath-taking image that evokes a sense of beauty, inspiration, awe or hope. 2. Menu Tabs Positioned Over the Image: • The menu tabs (navigation bar) should be positioned directly on top of the hero image, either centered or aligned to the top right/left, depending on the design. • The navigation bar should have a slightly transparent or solid background (depending on the image and visibility needs) to ensure the text is easily readable without detracting from the image. 3. Typography and Text Placement: • The text overlay on the hero image should use the selected fonts: • Cormorant Garamond for headers (e.g., the tagline or welcome message). • Source Sans Pro for any supporting text. 5. Seamless Transitions: • Below the full-width image, transitions into the next sections (like “About,” “Services,” or client-focused content) should be smooth, using full-width separators that maintain the cohesive, open layout style. 6. Color Palette: • A neutral and calming color palette should be used (e.g., soft blues, grays, whites, or very muted earth tones) to create a soothing atmosphere for visitors. This design approach ensures the homepage looks clean, modern, and professional while maintaining the calming and upscale aesthetic that reflects the values of my psychology practice

```html
<!DOCTYPE html>
<html lang="en">
<head>
<meta charset="utf-8">
<title>Dr. June Tillard – Licensed Psychologist</title>
<link rel="stylesheet" href="https://fonts.googleapis.com/css2?family=Marcellus&family=Source+Sans+3:wght@400;600;700&display=swap">
<style>
:root{
  --salmon:#d98b6e;
  --sage:#a8b69c;
  --ink:#2f2b29;
  --muted:#6b6461;
  --cream:#f4f3ef;
  --blush:#f7ebe2;
  --footer:#4a4543;
  --blue:#2f4b7b;
  --star:#f2a23a;
  --line:#d9d4cf;
}
*{box-sizing:border-box;margin:0;padding:0}
html,body{width:1200px;height:4317px;overflow:hidden}
body{font-family:"Source Sans 3",Arial,sans-serif;color:var(--ink);background:#fff;position:relative}
.serif{font-family:"Marcellus",Georgia,serif;font-weight:400}
.abs{position:absolute}
section,header,footer{position:absolute;left:0;width:1200px;overflow:hidden}
.btn{position:absolute;display:flex;align-items:center;justify-content:center;font-size:11px;color:#fff;border-radius:2px}
.btn.salmon{background:var(--salmon)}
.btn.sage{background:var(--sage)}
.photo{position:absolute;border-radius:10px}

.topbar{top:0;height:25px;background:var(--salmon)}
.topbar .soc{position:absolute;top:5px;width:15px;height:15px;border:1px solid #fff;border-radius:50%}
.nav{top:25px;height:62px;background:#fff}
.logo{position:absolute;left:100px;top:10px;line-height:1}
.logo .name{font-family:"Marcellus",Georgia,serif;font-size:22px}
.logo .role{font-family:"Marcellus",Georgia,serif;font-size:15px;margin-top:2px}
.nav .link{position:absolute;top:29px;font-size:11px;color:var(--ink)}
.call{position:absolute;left:958px;top:17px;display:flex;gap:8px;align-items:center}
.call .ico{width:26px;height:26px;border-radius:50%;background:var(--sage);display:flex;align-items:center;justify-content:center}
.call small{display:block;font-size:11px;color:var(--muted)}
.call b{font-size:14px;font-weight:700;color:var(--ink)}

.hero{top:87px;height:526px;background:
  radial-gradient(ellipse 420px 200px at 600px 60px,rgba(222,170,120,.75),transparent 70%),
  linear-gradient(180deg,#8b8a7a 0%,#56604e 30%,#2f3d30 60%,#1f2b22 100%)}
.hero h1{position:absolute;left:100px;top:150px;font-size:56px;line-height:60px;color:#fff}
.hero p{position:absolute;left:100px;top:285px;width:540px;font-size:12.5px;line-height:18px;color:#fff}

.services{top:613px;height:661px;background:var(--cream)}
.sec-title{position:absolute;left:0;width:1200px;text-align:center;font-size:42px}
.sec-sub{position:absolute;left:0;width:1200px;text-align:center;font-size:12px;color:var(--ink)}
.card-info{position:absolute;background:#fff;border-radius:8px;text-align:center;box-shadow:0 4px 14px rgba(0,0,0,.06)}
.card-info h3{font-size:22px;margin-top:46px}
.readmore{display:inline-flex;align-items:center;gap:6px;font-size:11px;color:var(--salmon);margin-top:10px}
.readmore i{width:14px;height:14px;border:1px solid var(--salmon);border-radius:50%;display:inline-block;position:relative}
.readmore i::after{content:"";position:absolute;left:4px;top:4px;width:4px;height:4px;border-top:1px solid var(--salmon);border-right:1px solid var(--salmon);transform:rotate(45deg)}
.badge{position:absolute;width:60px;height:60px;border-radius:50%;background:var(--sage);border:3px solid #fff}
.couples{position:absolute;left:439px;top:175px;width:322px;height:322px;background:var(--salmon);border-radius:8px}
.couples h3{position:absolute;top:187px;width:100%;text-align:center;font-size:22px;color:#fff}
.couples p{position:absolute;top:222px;left:30px;width:262px;text-align:center;font-size:11.5px;line-height:16px;color:#fff}
.arrow-c{position:absolute;width:38px;height:38px;border-radius:50%;background:#fff;border:1px solid var(--line);display:flex;align-items:center;justify-content:center}

.meet{top:1274px;height:633px;background:#fff}
.meet h2{position:absolute;left:618px;top:106px;font-size:40px;line-height:40px}
.meet .copy{position:absolute;left:618px;top:205px;width:475px;font-size:12px;line-height:19px}
.meet ul{list-style:none;margin:10px 0}
.meet li{position:relative;padding-left:12px;line-height:23px}
.meet li::before{content:"";position:absolute;left:2px;top:10px;width:3px;height:3px;border-radius:50%;background:var(--ink)}

.reviews{top:1907px;height:662px;background:var(--blush)}
.reviews h2{position:absolute;left:100px;top:214px;font-size:40px;line-height:40px}
.reviews .lead{position:absolute;left:100px;top:315px;width:420px;font-size:12px;line-height:20px}
.review{position:absolute;width:245px;height:218px;background:#fff;border-radius:6px;padding:18px 18px 0}
.stars{display:flex;gap:3px}
.stars svg{width:10px;height:10px}
.review h4{font-size:12px;font-weight:600;margin-top:10px}
.review p{font-size:10.5px;line-height:18px;color:var(--muted);margin-top:4px}
.review hr{border:0;border-top:1px solid var(--line);margin:10px 0 12px}
.who{display:flex;gap:12px;align-items:center}
.avatar{position:relative;width:36px;height:36px;border-radius:50%;background:#cfc8c2}
.avatar span{position:absolute;right:-3px;bottom:-3px;width:14px;height:14px;border-radius:50%;background:#fff;border:2px solid #9fb3d8}
.who b{display:block;font-size:12px}
.who small{font-size:10px;color:var(--muted)}

.blog{top:2569px;height:644px;background:#fff}
.post{position:absolute;top:180px;width:321px}
.post .pimg{height:204px;border-radius:10px;border-bottom:3px solid var(--salmon)}
.post h3{font-size:19px;color:var(--blue);margin-top:20px}
.post p{font-size:11.5px;line-height:19px;color:var(--muted);margin-top:6px}
.side-arrow{position:absolute;top:272px;font-size:18px;color:#9a9390}

.cta{top:3213px;height:248px;background:var(--salmon);text-align:center;color:#fff}
.cta h2{position:absolute;top:60px;width:100%;font-size:34px;line-height:40px}
.cta .btn{background:#fff;color:var(--salmon)}

.contact{top:3461px;height:519px;background:#fff}
.contact h2{position:absolute;left:100px;top:72px;font-size:34px}
.contact .sub{position:absolute;left:100px;top:128px;font-size:12px}
.field{position:absolute;border:1px solid #c9c3be;border-radius:3px;font-size:10px;color:#8e8884;padding:12px 16px}

.footer{top:3980px;height:337px;background:var(--footer);color:#fff}
.footer .fname{position:absolute;left:100px;top:64px;font-family:"Marcellus",Georgia,serif;font-size:22px;line-height:22px}
.footer .about{position:absolute;left:100px;top:117px;width:235px;font-size:10.5px;line-height:19px}
.footer .soc{position:absolute;top:225px;width:17px;height:17px;border:1px solid #fff;border-radius:50%}
.fcol{position:absolute;top:80px}
.fcol h5{font-family:"Marcellus",Georgia,serif;font-weight:400;font-size:14px;margin-bottom:14px}
.fcol a{display:block;font-size:11.5px;color:#fff;line-height:27.5px;text-decoration:none}
.cinfo{display:flex;align-items:center;gap:12px;font-size:11.5px;margin-bottom:14px}
.cinfo i{width:24px;height:24px;border-radius:50%;background:var(--salmon);display:flex;align-items:center;justify-content:center}
.footer .rule{position:absolute;left:100px;top:274px;width:999px;border-top:1px solid #7a7370}
.footer .copy{position:absolute;top:300px;width:100%;text-align:center;font-size:11px}
</style>
</head>
<body>

<header class="topbar">
  <span class="soc" style="left:1013px"></span>
  <span class="soc" style="left:1036px"></span>
  <span class="soc" style="left:1059px"></span>
  <span class="soc" style="left:1082px"></span>
</header>

<header class="nav">
  <div class="logo"><div class="name">Dr. June Tillard</div><div class="role">Licensed Psychologist</div></div>
  <span class="link" style="left:391px">Home</span>
  <span class="link" style="left:474px">Services ▾</span>
  <span class="link" style="left:578px">About Us</span>
  <span class="link" style="left:679px">Blog</span>
  <span class="link" style="left:754px">Contact Us</span>
  <div class="call">
    <span class="ico"><svg width="12" height="12" viewBox="0 0 24 24" fill="#fff"><path d="M6.6 10.8a15.1 15.1 0 0 0 6.6 6.6l2.2-2.2c.3-.3.7-.4 1-.2 1.1.4 2.3.6 3.6.6.6 0 1 .4 1 1V20c0 .6-.4 1-1 1A17 17 0 0 1 3 4c0-.6.4-1 1-1h3.5c.6 0 1 .4 1 1 0 1.3.2 2.5.6 3.6.1.3 0 .7-.2 1z"/></svg></span>
    <div><small>Call Us Anytime</small><b>(503) 555-0182</b></div>
  </div>
</header>

<section class="hero" role="img" aria-label="Misty mountain valley with pine forest at sunset">
  <h1 class="serif">Are You Struggling<br>with Life’s Challenges?</h1>
  <p>Dr. June Tillard and associates offer compassionate therapy to help you live, love, and work with purpose. Supporting individuals, couples, and families on their journey to meaningful change.</p>
  <span class="btn salmon" style="left:100px;top:349px;width:134px;height:33px">Schedule a Session</span>
  <span class="btn sage" style="left:252px;top:349px;width:168px;height:33px">Start Your Journey Today</span>
</section>

<section class="services">
  <h2 class="sec-title serif" style="top:68px">Our Therapy Services</h2>
  <p class="sec-sub" style="top:131px">Are you struggling with issues that affect the way you live, love or work?</p>

  <div class="photo" role="img" aria-label="Two hands reaching toward each other" style="left:100px;top:175px;width:321px;height:264px;background:linear-gradient(135deg,#6f7270,#b9bab6 50%,#5c5f5e)"></div>
  <div class="card-info" style="left:119px;top:401px;width:283px;height:114px">
    <h3 class="serif">Individual Therapy</h3>
    <span class="readmore">Read More <i></i></span>
  </div>
  <span class="badge" style="left:229px;top:371px"></span>

  <div class="couples">
    <div role="img" aria-label="Couple talking with a therapist on a sofa" style="position:absolute;left:0;top:0;width:322px;height:134px;border-radius:8px 8px 0 0;background:linear-gradient(135deg,#d9cbbd,#a27a62 60%,#5c4b42)"></div>
    <span class="badge" style="left:131px;top:104px"></span>
    <h3 class="serif">Couples Therapy</h3>
    <p>We help couples understand how the distress in their relationship is caused by cycles of disconnection in which married couples often find themselves stuck.</p>
    <span class="arrow-c" style="left:142px;top:301px"><svg width="14" height="10" viewBox="0 0 14 10" fill="none" stroke="#555" stroke-width="1.2"><path d="M0 5h13M9 1l4 4-4 4"/></svg></span>
  </div>

  <div class="photo" role="img" aria-label="Family sitting together with a counselor" style="left:779px;top:175px;width:321px;height:264px;background:linear-gradient(135deg,#cfc9c1,#8b8580 55%,#5f5a57)"></div>
  <div class="card-info" style="left:798px;top:401px;width:283px;height:114px">
    <h3 class="serif">Family Counseling</h3>
    <span class="readmore">Read More <i></i></span>
  </div>
  <span class="badge" style="left:908px;top:371px"></span>

  <span class="btn salmon" style="left:439px;top:547px;width:141px;height:33px">Schedule a Session</span>
  <span class="btn sage" style="left:593px;top:547px;width:168px;height:33px">Start Your Journey Today</span>
</section>

<section class="meet">
  <div class="photo" role="img" aria-label="Portrait of Dr. June Tillard in her office" style="left:100px;top:82px;width:468px;height:469px;background:linear-gradient(135deg,#d8d6d1,#b8a99c 45%,#3a3433 75%,#cfcac4)"></div>
  <h2 class="serif">Meet Dr. June Tillard<br>and Associates</h2>
  <div class="copy">
    <p>Dr. June Tillard and her associates are licensed psychologists in Ashgrove, Oregon. We offer therapy for individuals, couples and families to help you create meaningful change, whether you:</p>
    <ul>
      <li>Feel overwhelmed with depression or anxiety.</li>
      <li>Experience a lack of connection in your marriage.</li>
      <li>Worry excessively about what others think.</li>
      <li>Have a history of trauma or abuse.</li>
      <li>Parent a child with complex needs.</li>
      <li>Struggle with other life challenges.</li>
    </ul>
    <p>We have extensive experience treating a full spectrum of mental health disorders using a collaborative and compassionate approach. In addition to individual therapy, we also provide couples counseling and family therapy.</p>
  </div>
  <span class="btn salmon" style="left:618px;top:491px;width:140px;height:31px">Schedule a Session</span>
  <span class="btn sage" style="left:770px;top:491px;width:148px;height:31px">Read More About Me</span>
</section>

<section class="reviews">
  <h2 class="serif">What Our Clients Says<br>About Us</h2>
  <p class="lead">Lorem Ipsum is simply dummy text of the printing and typesetting industry. Ipsum has been the industry's standard dummy text ever since an unknown printer took a galley of type and scrambled it to make a type specimen book.</p>
  <span class="btn salmon" style="left:100px;top:398px;width:133px;height:32px">View More Review</span>

  <div class="review" style="left:590px;top:84px">
    <div class="stars"><svg viewBox="0 0 10 10"><path fill="var(--star)" d="M5 0l1.5 3.2 3.5.4-2.6 2.4.7 3.5L5 7.8 1.9 9.5l.7-3.5L0 3.6l3.5-.4z"/></svg><svg viewBox="0 0 10 10"><path fill="var(--star)" d="M5 0l1.5 3.2 3.5.4-2.6 2.4.7 3.5L5 7.8 1.9 9.5l.7-3.5L0 3.6l3.5-.4z"/></svg><svg viewBox="0 0 10 10"><path fill="var(--star)" d="M5 0l1.5 3.2 3.5.4-2.6 2.4.7 3.5L5 7.8 1.9 9.5l.7-3.5L0 3.6l3.5-.4z"/></svg><svg viewBox="0 0 10 10"><path fill="var(--star)" d="M5 0l1.5 3.2 3.5.4-2.6 2.4.7 3.5L5 7.8 1.9 9.5l.7-3.5L0 3.6l3.5-.4z"/></svg><svg viewBox="0 0 10 10"><path fill="var(--star)" d="M5 0l1.5 3.2 3.5.4-2.6 2.4.7 3.5L5 7.8 1.9 9.5l.7-3.5L0 3.6l3.5-.4z"/></svg></div>
    <h4>Healing is a priority</h4>
    <p>Lorem Ipsum has been the industry's standard dummy text ever since the 1500s, when an unknown printer took a galley of type and scrambled...</p>
    <hr>
    <div class="who"><span class="avatar" role="img" aria-label="Reviewer photo"><span></span></span><div><b>Lena Marsh</b><small>Lorem Ipsum</small></div></div>
  </div>
  <div class="review" style="left:590px;top:322px">
    <div class="stars"><svg viewBox="0 0 10 10"><path fill="var(--star)" d="M5 0l1.5 3.2 3.5.4-2.6 2.4.7 3.5L5 7.8 1.9 9.5l.7-3.5L0 3.6l3.5-.4z"/></svg><svg viewBox="0 0 10 10"><path fill="var(--star)" d="M5 0l1.5 3.2 3.5.4-2.6 2.4.7 3.5L5 7.8 1.9 9.5l.7-3.5L0 3.6l3.5-.4z"/></svg><svg viewBox="0 0 10 10"><path fill="var(--star)" d="M5 0l1.5 3.2 3.5.4-2.6 2.4.7 3.5L5 7.8 1.9 9.5l.7-3.5L0 3.6l3.5-.4z"/></svg><svg viewBox="0 0 10 10"><path fill="var(--star)" d="M5 0l1.5 3.2 3.5.4-2.6 2.4.7 3.5L5 7.8 1.9 9.5l.7-3.5L0 3.6l3.5-.4z"/></svg><svg viewBox="0 0 10 10"><path fill="var(--star)" d="M5 0l1.5 3.2 3.5.4-2.6 2.4.7 3.5L5 7.8 1.9 9.5l.7-3.5L0 3.6l3.5-.4z"/></svg></div>
    <h4>Healing is a priority</h4>
    <p>Lorem Ipsum has been the industry's standard dummy text ever since the 1500s, when an unknown printer took a galley of type and scrambled...</p>
    <hr>
    <div class="who"><span class="avatar" role="img" aria-label="Reviewer photo"><span></span></span><div><b>Lena Marsh</b><small>Lorem Ipsum</small></div></div>
  </div>
  <div class="review" style="left:855px;top:123px">
    <div class="stars"><svg viewBox="0 0 10 10"><path fill="var(--star)" d="M5 0l1.5 3.2 3.5.4-2.6 2.4.7 3.5L5 7.8 1.9 9.5l.7-3.5L0 3.6l3.5-.4z"/></svg><svg viewBox="0 0 10 10"><path fill="var(--star)" d="M5 0l1.5 3.2 3.5.4-2.6 2.4.7 3.5L5 7.8 1.9 9.5l.7-3.5L0 3.6l3.5-.4z"/></svg><svg viewBox="0 0 10 10"><path fill="var(--star)" d="M5 0l1.5 3.2 3.5.4-2.6 2.4.7 3.5L5 7.8 1.9 9.5l.7-3.5L0 3.6l3.5-.4z"/></svg><svg viewBox="0 0 10 10"><path fill="var(--star)" d="M5 0l1.5 3.2 3.5.4-2.6 2.4.7 3.5L5 7.8 1.9 9.5l.7-3.5L0 3.6l3.5-.4z"/></svg><svg viewBox="0 0 10 10"><path fill="var(--star)" d="M5 0l1.5 3.2 3.5.4-2.6 2.4.7 3.5L5 7.8 1.9 9.5l.7-3.5L0 3.6l3.5-.4z"/></svg></div>
    <h4>Healing is a priority</h4>
    <p>Lorem Ipsum has been the industry's standard dummy text ever since the 1500s, when an unknown printer took a galley of type and scrambled ...</p>
    <hr>
    <div class="who"><span class="avatar" role="img" aria-label="Reviewer photo"><span></span></span><div><b>Lena Marsh</b><small>Lorem Ipsum</small></div></div>
  </div>
  <div class="review" style="left:855px;top:361px">
    <div class="stars"><svg viewBox="0 0 10 10"><path fill="var(--star)" d="M5 0l1.5 3.2 3.5.4-2.6 2.4.7 3.5L5 7.8 1.9 9.5l.7-3.5L0 3.6l3.5-.4z"/></svg><svg viewBox="0 0 10 10"><path fill="var(--star)" d="M5 0l1.5 3.2 3.5.4-2.6 2.4.7 3.5L5 7.8 1.9 9.5l.7-3.5L0 3.6l3.5-.4z"/></svg><svg viewBox="0 0 10 10"><path fill="var(--star)" d="M5 0l1.5 3.2 3.5.4-2.6 2.4.7 3.5L5 7.8 1.9 9.5l.7-3.5L0 3.6l3.5-.4z"/></svg><svg viewBox="0 0 10 10"><path fill="var(--star)" d="M5 0l1.5 3.2 3.5.4-2.6 2.4.7 3.5L5 7.8 1.9 9.5l.7-3.5L0 3.6l3.5-.4z"/></svg><svg viewBox="0 0 10 10"><path fill="var(--star)" d="M5 0l1.5 3.2 3.5.4-2.6 2.4.7 3.5L5 7.8 1.9 9.5l.7-3.5L0 3.6l3.5-.4z"/></svg></div>
    <h4>Healing is a priority</h4>
    <p>Lorem Ipsum has been the industry's standard dummy text ever since the 1500s, when an unknown printer took a galley of type and scrambled ....</p>
    <hr>
    <div class="who"><span class="avatar" role="img" aria-label="Reviewer photo"><span></span></span><div><b>Lena Marsh</b><small>Lorem Ipsum</small></div></div>
  </div>
</section>

<section class="blog">
  <h2 class="sec-title serif" style="top:72px">Our Latest Blog</h2>
  <p class="sec-sub" style="top:133px">Are you struggling with issues that affect the way you live, love or work?</p>
  <span class="side-arrow" style="left:68px">←</span>
  <span class="side-arrow" style="left:1117px">→</span>

  <article class="post" style="left:100px">
    <div class="pimg" role="img" aria-label="Sunbeams through a misty forest" style="background:linear-gradient(135deg,#d8c8a4,#8a6f45 50%,#3f3426)"></div>
    <h3 class="serif">Lorem Ipsum is simply dummy</h3>
    <p>Lorem Ipsum is simply dummy text of the printing and typesetting industry. Lorem Ipsum is simply dummy text of the printing and typesetting industry.</p>
    <span class="readmore">Read More <i></i></span>
  </article>
  <article class="post" style="left:440px">
    <div class="pimg" role="img" aria-label="Therapist and client in conversation" style="background:linear-gradient(135deg,#ece6de,#c8b7a4 55%,#6a6f7a)"></div>
    <h3 class="serif">Lorem Ipsum is simply dummy</h3>
    <p>Lorem Ipsum is simply dummy text of the printing and typesetting industry. Lorem Ipsum is simply dummy text of the printing and typesetting industry.</p>
    <span class="readmore">Read More <i></i></span>
  </article>
  <article class="post" style="left:779px">
    <div class="pimg" role="img" aria-label="Couple seated with a counselor" style="background:linear-gradient(135deg,#cfc6b8,#8a7160 55%,#4d4a48)"></div>
    <h3 class="serif">Lorem Ipsum is simply dummy</h3>
    <p>Lorem Ipsum is simply dummy text of the printing and typesetting industry. Lorem Ipsum is simply dummy text of the printing and typesetting industry.</p>
    <span class="readmore">Read More <i></i></span>
  </article>

  <span class="btn sage" style="left:537px;top:549px;width:126px;height:33px">View More Blogs</span>
</section>

<section class="cta">
  <h2 class="serif">Don’t Know Where To Start?<br>Call At (503) 555-0182</h2>
  <span class="btn" style="left:549px;top:152px;width:102px;height:33px">Call Us Now</span>
</section>

<section class="contact">
  <h2 class="serif">Get In Touch With Us</h2>
  <p class="sub">Contact us to schedule a demo to learn more.</p>
  <div class="field" style="left:100px;top:164px;width:252px;height:37px">First Name</div>
  <div class="field" style="left:367px;top:164px;width:253px;height:37px">Last Name</div>
  <div class="field" style="left:100px;top:214px;width:252px;height:37px">Email</div>
  <div class="field" style="left:367px;top:214px;width:253px;height:37px">Phone</div>
  <div class="field" style="left:100px;top:265px;width:520px;height:120px">Message</div>
  <span class="btn sage" style="left:100px;top:405px;width:103px;height:33px">Submit Now</span>
  <div class="photo" role="img" aria-label="Smiling support advisor with headset at a laptop" style="left:670px;top:64px;width:429px;height:393px;background:linear-gradient(135deg,#f1f1ef,#dfe3e6 45%,#a7b8cf 75%,#8a7b6f)"></div>
</section>

<footer class="footer">
  <div class="fname">Dr. June Tillard<br><span style="font-size:16px">Licensed Psychologist</span></div>
  <p class="about">We have extensive experience treating a full spectrum of mental health disorders using a collaborative and compassionate approach. In addition to individual therapy, we also provide couples counseling and family therapy.</p>
  <span class="soc" style="left:100px"></span>
  <span class="soc" style="left:122px"></span>
  <span class="soc" style="left:144px"></span>
  <span class="soc" style="left:166px"></span>

  <div class="fcol" style="left:416px;top:83px">
    <h5>Quick links</h5>
    <a>Home</a><a>Services</a><a>About Us</a><a>Blog</a><a>Contact Us</a>
  </div>
  <div class="fcol" style="left:570px;top:83px">
    <h5>Contact Info</h5>
    <div class="cinfo"><i><svg width="11" height="11" viewBox="0 0 24 24" fill="#fff"><path d="M6.6 10.8a15.1 15.1 0 0 0 6.6 6.6l2.2-2.2c.3-.3.7-.4 1-.2 1.1.4 2.3.6 3.6.6.6 0 1 .4 1 1V20c0 .6-.4 1-1 1A17 17 0 0 1 3 4c0-.6.4-1 1-1h3.5c.6 0 1 .4 1 1 0 1.3.2 2.5.6 3.6.1.3 0 .7-.2 1z"/></svg></i>(503) 555-0182</div>
    <div class="cinfo"><i><svg width="11" height="9" viewBox="0 0 22 16" fill="none" stroke="#fff" stroke-width="2"><rect x="1" y="1" width="20" height="14" rx="1"/><path d="M1 1l10 8 10-8"/></svg></i>hello@junetillard.com</div>
  </div>
  <div class="fcol" style="left:846px;top:83px">
    <h5>Subscribe Newsletter</h5>
  </div>
  <div class="abs" style="left:846px;top:106px;width:253px;height:35px;background:#fff;border-radius:3px;font-size:10px;color:#8e8884;padding:11px 16px">Email</div>
  <span class="btn salmon" style="left:846px;top:153px;width:253px;height:32px">Submit Now</span>

  <div class="rule"></div>
  <p class="copy">© Copyright All Right Reserved.2025</p>
</footer>

</body>
</html>
```